Creation of a book cover
Size : 14 x 20,5 cm (+ 5 mm bleed area at the top, bottom and right areas)
The Title is a French sentence which means “The heron dreaming on the cold roof of this empty station”. It’s a surrealistic title which has no link to the story.
AUTHOR : Mathieu Vorlange
TITLE : "Le héron rêvant sur le toit froid de cette gare vide »
PUBLISHER (AT THE BOTTOM OF THE PAGE) : Editions Parvenche
I send a PDF file with the kind of cover we have imagine, but you can propose something different. The glass and the fly can of course be used.

```html
<!DOCTYPE html>
<html lang="fr">
<head>
<meta charset="utf-8">
<title>Le héron rêvant sur le toit froid de cette gare vide — Mathieu Vorlange</title>
<link rel="stylesheet" href="https://fonts.googleapis.com/css2?family=Italiana&family=Rubik+Dirt&family=Courier+Prime:wght@700&display=swap">
<style>
  :root {
    --backdrop: #858585;
    --paper: #ffffff;
    --ink: #141414;
    --title-red: #8e1616;
    --glitch-magenta: #e11ee6;
    --glitch-green: #22e05a;
    --art-light: #f1f1f1;
    --art-mid: #b9bdb9;
    --art-dark: #3a3a3a;
  }
  * { margin: 0; padding: 0; box-sizing: border-box; }
  html, body {
    width: 1200px;
    height: 2667px;
    overflow: hidden;
    background: var(--backdrop);
  }
  .cover {
    position: absolute;
    left: 10px;
    top: 486px;
    width: 1180px;
    height: 1694px;
    background: var(--paper);
    overflow: hidden;
  }
  .cover__author {
    position: absolute;
    top: 118px;
    left: 0;
    width: 100%;
    text-align: center;
    font-family: "Italiana", serif;
    font-size: 78px;
    letter-spacing: 3px;
    color: var(--ink);
  }
  .cover__title {
    position: absolute;
    top: 405px;
    left: 0;
    width: 100%;
    text-align: center;
    font-family: "Rubik Dirt", sans-serif;
    font-size: 138px;
    line-height: 1;
    color: var(--title-red);
    letter-spacing: 2px;
  }
  .phrase {
    position: absolute;
    font-family: "Courier Prime", monospace;
    font-weight: 700;
    font-size: 78px;
    line-height: 1;
    color: var(--ink);
    white-space: nowrap;
  }
  .phrase--glitch {
    text-shadow: 3px 3px 0 var(--glitch-magenta), -3px -2px 0 var(--glitch-green);
  }
  .phrase--top {
    left: 325px;
    top: 620px;
    transform: rotate(-9deg);
    transform-origin: left bottom;
  }
  .phrase--left {
    left: 285px;
    top: 820px;
    writing-mode: vertical-rl;
  }
  .phrase--right {
    left: 782px;
    top: 975px;
    writing-mode: vertical-rl;
  }
  .phrase--bottom {
    left: 335px;
    top: 1318px;
    transform: rotate(4deg);
    transform-origin: left top;
  }
  .cover__art {
    position: absolute;
    left: 362px;
    top: 688px;
    width: 440px;
    height: 600px;
    background: radial-gradient(ellipse at 50% 40%, var(--art-mid) 0%, var(--art-light) 70%, var(--paper) 100%);
    border-radius: 40px;
  }
  .cover__publisher {
    position: absolute;
    top: 1490px;
    left: 0;
    width: 100%;
    text-align: center;
    font-family: "Italiana", serif;
    font-size: 46px;
    letter-spacing: 4px;
    color: var(--ink);
  }
</style>
</head>
<body>
  <main class="cover">
    <p class="cover__author">Mathieu Vorlange</p>
    <h1 class="cover__title">LE HÉRON</h1>
    <div class="cover__art" role="img" aria-label="Illustration gravée d’un héron perché sur le toit d’une petite gare vide"></div>
    <p class="phrase phrase--top">rêvant sur le</p>
    <p class="phrase phrase--left">toit froid</p>
    <p class="phrase phrase--right phrase--glitch">de cette</p>
    <p class="phrase phrase--bottom phrase--glitch">gare vide</p>
    <p class="cover__publisher">EDITIONS PARVENCHE</p>
  </main>
</body>
</html>
```